Brightwire Hollow Business cards

one side I would like my logo (uploaded) and the other side I want my details. I'm an electrician in sydney. The logo side I'm happy with just a white background and our logo in the middle.

Details for other side
24/7 Sydney Electrician
Marcus Pell
0431 587 219
marcus@brightwirehollow.com.au
brightwirehollow.com.au
icons for facebook, instagram, linked in

Industry/Entity Type

electrician

Contact Information for Business Card

company info

```html
<!DOCTYPE html>
<html lang="en">
<head>
<meta charset="utf-8">
<title>Brightwire Hollow – Business Cards</title>
<link rel="stylesheet" href="https://fonts.googleapis.com/css2?family=Chakra+Petch:wght@500;600;700&display=swap">
<style>
  :root {
    --backdrop: #e0e3fd;
    --card-white: #ffffff;
    --brand-red: #ee2b2e;
    --ink: #121212;
    --text-light: #f4f4f4;
    --tab-grey-top: #2a2a2a;
    --tab-grey-bottom: #5c5c5c;
  }
  * { box-sizing: border-box; margin: 0; padding: 0; }
  html, body {
    width: 1200px; height: 1200px; overflow: hidden;
    background: var(--backdrop);
  }
  .sheet { position: relative; width: 1200px; height: 1200px; }

  .card {
    position: absolute; left: 243px; width: 714px; height: 479px;
    background: var(--card-white); overflow: hidden;
  }
  .card--front { top: 81px; }
  .card--back { top: 640px; }

  .wordmark {
    position: absolute; left: 0; right: 0;
    text-align: center;
    font-family: "Chakra Petch", sans-serif; font-weight: 700;
    color: var(--brand-red);
    text-transform: uppercase; line-height: 0.95;
    letter-spacing: 2px;
  }
  .card--front .wordmark { top: 188px; font-size: 50px; }
  .card--back .wordmark { top: 78px; font-size: 42px; }

  .top-tab {
    position: absolute; left: 142px; top: 0; width: 429px; height: 47px;
    background: var(--brand-red);
    border-radius: 0 0 27px 27px;
  }

  .details-panel {
    position: absolute; left: 0; top: 188px; width: 100%; bottom: 0;
    background: var(--ink);
  }
  .contact-name {
    position: absolute; left: 0; right: 0; top: 13px;
    text-align: center; color: var(--text-light);
    font-family: "Chakra Petch", sans-serif; font-weight: 500;
    font-size: 21px; letter-spacing: 1.5px;
  }
  .contact-line {
    position: absolute; left: 0; right: 0;
    display: flex; justify-content: center; align-items: center; gap: 12px;
    color: var(--text-light);
    font-family: "Chakra Petch", sans-serif; font-weight: 600;
    letter-spacing: 1.3px;
  }
  .contact-line svg { flex: none; }
  .contact-line--phone { top: 51px; font-size: 19px; }
  .contact-line--email { top: 89px; font-size: 16px; }
  .contact-line--web { top: 124px; font-size: 16px; }

  .social-row {
    position: absolute; left: 0; right: 0; top: 173px;
    display: flex; justify-content: center; gap: 9px;
  }
  .social-dot {
    width: 19px; height: 19px; border-radius: 50%;
    background: var(--brand-red);
  }

  .footer-band {
    position: absolute; top: 393px; height: 36px; background: var(--brand-red);
  }
  .footer-band--left { left: 0; width: 142px; }
  .footer-band--right { right: 0; width: 142px; }
  .tagline-tab {
    position: absolute; left: 142px; top: 393px; width: 430px; height: 49px;
    background: linear-gradient(var(--tab-grey-top), var(--tab-grey-bottom));
    border-radius: 0 0 27px 27px;
    display: flex; justify-content: center; align-items: center;
    padding-bottom: 8px;
    color: var(--text-light);
    font-family: "Chakra Petch", sans-serif; font-weight: 700;
    font-size: 12px; letter-spacing: 4.5px;
  }
</style>
</head>
<body>
<main class="sheet">
  <section class="card card--front" aria-label="Card front">
    <div class="wordmark">Brightwire<br>Hollow</div>
  </section>

  <section class="card card--back" aria-label="Card back">
    <div class="top-tab"></div>
    <div class="wordmark">Brightwire<br>Hollow</div>

    <div class="details-panel">
      <p class="contact-name">Marcus Pell</p>

      <p class="contact-line contact-line--phone">
        <svg width="16" height="18" viewBox="0 0 24 24" aria-hidden="true">
          <path fill="#ee2b2e" d="M6.6 10.8a15.1 15.1 0 0 0 6.6 6.6l2.2-2.2c.3-.3.7-.4 1-.2 1.1.4 2.3.6 3.6.6.6 0 1 .4 1 1V20c0 .6-.4 1-1 1A17 17 0 0 1 3 4c0-.6.4-1 1-1h3.5c.6 0 1 .4 1 1 0 1.3.2 2.5.6 3.6.1.3 0 .7-.2 1z"/>
        </svg>
        0431 587 219
      </p>

      <p class="contact-line contact-line--email">
        <svg width="19" height="13" viewBox="0 0 19 13" aria-hidden="true">
          <rect width="19" height="13" fill="#ee2b2e"/>
          <path d="M0.5 0.8 9.5 7.5 18.5 0.8M0.5 12.3 7 6.2M18.5 12.3 12 6.2" fill="none" stroke="#121212" stroke-width="1"/>
        </svg>
        marcus@brightwirehollow.com.au
      </p>

      <p class="contact-line contact-line--web">
        <svg width="16" height="16" viewBox="0 0 16 16" aria-hidden="true">
          <circle cx="8" cy="8" r="8" fill="#ee2b2e"/>
          <path d="M8 0.5v15M0.5 8h15M8 0.5c-3.5 3.5-3.5 11.5 0 15M8 0.5c3.5 3.5 3.5 11.5 0 15" fill="none" stroke="#121212" stroke-width="1"/>
        </svg>
        brightwirehollow.com.au
      </p>

      <div class="social-row">
        <span class="social-dot" role="img" aria-label="Social profile link"></span>
        <span class="social-dot" role="img" aria-label="Social profile link"></span>
        <span class="social-dot" role="img" aria-label="Social profile link"></span>
      </div>
    </div>

    <div class="footer-band footer-band--left"></div>
    <div class="footer-band footer-band--right"></div>
    <div class="tagline-tab">24/7 SYDNEY ELECTRICIAN</div>
  </section>
</main>
</body>
</html>
```